Wine label required for an organic wine

We require a wine label to represent a new organic wine. The label must have earthy and natural tones yet be modern and contemporary. Authentic branding is the key and is to be based on the company's culture and journey to environmental sustainability. http://www.morvaleen.com.au/our-story/carbon-balanced.html
A stand alone, bold and stylish label to reflect an organic wine. This wine is a premium retail wine offering to sell for approx. $25(AUD).

Target Market(s)

25-40 year olds with wider appeal to consumers looking for healthier and more natural practices for an environmentally responsible lifestyle

Number of Pages Required

1 page

Font styles to use
Sans Serif

Colors

Designer to choose colors to be used in the design.

Requirements
Must have
• Authenticity
• modern and contemporary
• link to the fact that it is an organic wine

```html
<!DOCTYPE html>
<html lang="en">
<head>
<meta charset="utf-8">
<title>Morvaleen Organic Wine Labels</title>
<link rel="stylesheet" href="https://fonts.googleapis.com/css2?family=Josefin+Sans:wght@400&family=Pinyon+Script&display=swap">
<style>
  :root {
    --canvas: #f4f3f0;
    --label-paper: #f7f6f3;
    --label-edge: #dcd9d3;
    --shiraz: #8a2a3a;
    --chardonnay: #3e7a52;
    --ink-grey: #6f6d6a;
    --stamp-grey: #a9a6a1;
  }
  * { box-sizing: border-box; margin: 0; padding: 0; }
  html, body {
    width: 900px; height: 1200px; overflow: hidden;
    background: var(--canvas);
  }
  .label-sheet {
    width: 900px; height: 1200px;
    display: flex; flex-direction: column;
    align-items: center; justify-content: center; gap: 90px;
  }
  .wine-label {
    position: relative;
    width: 660px; height: 440px;
    background: var(--label-paper);
    border: 1px solid var(--label-edge);
    box-shadow: 0 2px 10px rgba(0,0,0,0.06);
    overflow: hidden;
  }
  .grape-vine-art {
    position: absolute; left: 0; right: 0; top: 0; height: 230px;
    -webkit-mask-image: linear-gradient(to bottom, #000 55%, transparent 100%);
            mask-image: linear-gradient(to bottom, #000 55%, transparent 100%);
  }
  .wine-label--shiraz .grape-vine-art {
    background: linear-gradient(100deg, rgba(123,58,99,0.55) 0%, rgba(201,138,167,0.35) 30%, rgba(185,211,184,0.35) 55%, rgba(123,58,99,0.45) 80%, rgba(201,138,167,0.3) 100%);
  }
  .wine-label--chardonnay .grape-vine-art {
    background: linear-gradient(100deg, rgba(92,154,110,0.5) 0%, rgba(185,211,184,0.4) 30%, rgba(201,138,167,0.3) 55%, rgba(92,154,110,0.45) 80%, rgba(185,211,184,0.35) 100%);
  }
  .brand-mark {
    position: absolute; top: 24px; left: 0; right: 0;
    display: flex; flex-direction: column; align-items: center; gap: 6px;
  }
  .brand-mark__dot {
    width: 44px; height: 44px; border-radius: 50%;
    background: var(--ink-grey);
  }
  .brand-mark__name {
    font-family: "Josefin Sans", sans-serif; font-weight: 400;
    font-size: 15px; letter-spacing: 4px;
    color: var(--ink-grey);
  }
  .brand-mark__tagline {
    font-family: "Josefin Sans", sans-serif; font-weight: 400;
    font-size: 10px; letter-spacing: 3px;
    color: var(--ink-grey);
  }
  .variety-block {
    position: absolute; left: 0; right: 0; top: 215px;
    text-align: center;
  }
  .variety-name {
    font-family: "Pinyon Script", cursive;
    font-weight: 400; line-height: 1;
  }
  .wine-label--shiraz .variety-name { color: var(--shiraz); font-size: 96px; }
  .wine-label--chardonnay .variety-name { color: var(--chardonnay); font-size: 80px; }
  .vintage {
    margin-top: 12px;
    font-family: "Josefin Sans", sans-serif; font-weight: 400;
    font-size: 18px; letter-spacing: 4px;
    color: var(--ink-grey);
  }
  .organic-seal {
    position: absolute; left: 28px; bottom: 40px;
    width: 74px; height: 74px;
  }
</style>
</head>
<body>
  <main class="label-sheet">
    <section class="wine-label wine-label--shiraz">
      <div class="grape-vine-art" role="img" aria-label="Watercolour vine with purple and pink grape clusters and green leaves"></div>
      <div class="brand-mark">
        <span class="brand-mark__dot"></span>
        <span class="brand-mark__name">MORVALEEN</span>
        <span class="brand-mark__tagline">ORGANIC</span>
      </div>
      <div class="variety-block">
        <h2 class="variety-name">Shiraz</h2>
        <p class="vintage">2020</p>
      </div>
      <svg class="organic-seal" viewBox="0 0 100 100" aria-hidden="true">
        <circle cx="50" cy="50" r="46" fill="none" stroke="var(--stamp-grey)" stroke-width="4"/>
        <circle cx="50" cy="50" r="34" fill="none" stroke="var(--stamp-grey)" stroke-width="2"/>
      </svg>
    </section>

    <section class="wine-label wine-label--chardonnay">
      <div class="grape-vine-art" role="img" aria-label="Watercolour vine with green grape clusters and leaves"></div>
      <div class="brand-mark">
        <span class="brand-mark__dot"></span>
        <span class="brand-mark__name">MORVALEEN</span>
        <span class="brand-mark__tagline">ORGANIC</span>
      </div>
      <div class="variety-block">
        <h2 class="variety-name">Chardonnay</h2>
        <p class="vintage">2020</p>
      </div>
      <svg class="organic-seal" viewBox="0 0 100 100" aria-hidden="true">
        <circle cx="50" cy="50" r="46" fill="none" stroke="var(--stamp-grey)" stroke-width="4"/>
        <circle cx="50" cy="50" r="34" fill="none" stroke="var(--stamp-grey)" stroke-width="2"/>
      </svg>
    </section>
  </main>
</body>
</html>
```